VORNAK (PTY)LTD Website design

WEBSITE design based on our different divisions in our organization.
Our company specializes in the following.
Construction
Property development
Demolition
Mining
Transport
Manufacturing of concrete bricks and blocks
Lightweight concrete Readymix
I want a very modern website and look that fits in with our organization and the changing times of the world.
The website must be very professional and crisp and should appeal to both the younger generation and older generation of business leaders and.
The website must be very user friendly and easy to navigate, simple yet modern, professional and corporate.

```html
<!DOCTYPE html>
<html lang="en">
<head>
<meta charset="utf-8">
<title>VORNAK (PTY)LTD</title>
<link href="https://fonts.googleapis.com/css2?family=Oswald:wght@500&family=Poppins:wght@400;500;600;700&display=swap" rel="stylesheet">
<style>
:root{
  --blue:#138dcc;
  --black:#050505;
  --dark:#222222;
  --footer:#0c0c0c;
  --grey:#6a6a6a;
  --text:#333333;
  --line:#dcdcdc;
  --white:#ffffff;
}
*{box-sizing:border-box;margin:0;padding:0}
html,body{width:1200px;height:3448px;overflow:hidden}
body{position:relative;font-family:"Poppins",sans-serif;color:var(--text);background:var(--white)}
.abs{position:absolute}
.header{left:0;top:0;width:1200px;height:110px;background:var(--black)}
.brand{font-family:"Poppins",sans-serif;font-weight:700;color:var(--blue);font-size:54px;letter-spacing:2px;line-height:1}
.header .brand{left:112px;top:22px}
.top-contact{top:14px;font-size:13px;color:var(--white);display:flex;align-items:center;gap:6px}
.top-contact i{width:9px;height:9px;border-radius:50%;background:var(--blue);display:inline-block}
.main-nav{top:72px;font-size:14px;color:var(--white);font-weight:500}
.hero{left:0;top:110px;width:1200px;height:680px;background:linear-gradient(100deg,#e9e9e7 0%,#f1efe9 35%,#d8c3a0 60%,#f4f2ee 80%,#cfd6cc 100%)}
.hero-title{left:115px;top:290px;font-family:"Oswald",sans-serif;font-weight:500;font-size:58px;line-height:66px;color:#2c2c2c;letter-spacing:1px}
.btn{background:var(--blue);color:var(--white);font-weight:600;font-size:12px;letter-spacing:.5px;display:flex;align-items:center;justify-content:center}
.hero-btn{left:115px;top:444px;width:147px;height:50px}
.slide-arrow{top:356px;width:36px;height:38px;background:#3a3a3a}
.section-title{left:0;width:1200px;text-align:center;font-size:36px;font-weight:600;letter-spacing:.5px}
.section-title .soft{color:var(--grey)}
.rule{left:113px;width:974px;height:1px;background:var(--line)}
.rule-dot{left:595px;width:10px;height:10px;border-radius:50%;background:var(--blue)}
.lead{left:113px;width:974px;text-align:center;font-size:11.5px;line-height:28px;color:var(--text)}
.pillar-title{font-size:17px;font-weight:600;color:var(--dark)}
.pillar-title .soft{color:var(--grey);font-weight:500}
.pillar-text{font-size:11.5px;line-height:23px;width:345px}
.read-btn{left:545px;top:1249px;width:110px;height:32px;background:var(--black);font-size:11px}
.services{left:0;top:1360px;width:1200px;height:686px;background:var(--dark)}
.services-title{top:1428px;color:var(--white)}
.hex-label{left:115px;top:1630px;width:230px;text-align:center;color:var(--white)}
.hex-label h3{font-size:21px;font-weight:700;line-height:26px}
.hex-label p{font-size:11.5px;line-height:20px;margin-top:6px}
.testi-title{top:2216px;color:var(--dark)}
.quote{left:170px;top:2510px;width:860px;text-align:center;font-size:11.5px;line-height:28px}
.quote-mark{font-size:110px;line-height:1;color:#cfcfcf;font-family:"Poppins",sans-serif;font-weight:700}
.client-name{left:0;top:2616px;width:1200px;text-align:center;font-size:12px;font-weight:600;color:var(--dark)}
.client-role{left:0;top:2644px;width:1200px;text-align:center;font-size:10.5px;color:var(--grey)}
.footer-bg{left:0;top:2840px;width:1200px;height:544px;background:var(--footer)}
.footer .brand{left:0;top:2860px;width:1200px;text-align:center;font-size:72px}
.foot-h{font-size:21px;font-weight:600;color:var(--white);letter-spacing:.5px}
.foot-text{font-size:12px;line-height:19px;color:var(--white)}
.addr-row{left:113px;display:flex;gap:12px;align-items:flex-start}
.addr-row svg{flex:none;margin-top:2px}
.field{background:var(--white);height:36px;left:703px;width:385px;font-size:12px;color:var(--text);padding:8px 8px}
.sub-input{left:430px;top:3074px;width:225px;height:34px;background:#3b3b3b}
.social{top:3274px;display:flex;gap:28px;left:113px;align-items:center}
.social i{display:block;border-radius:50%}
.bottom-nav{left:0;top:3384px;width:1200px;height:64px;background:var(--blue)}
.bottom-nav span{position:absolute;top:22px;font-size:14px;color:var(--white);font-weight:500}
</style>
</head>
<body>

<!-- Header -->
<header class="abs header">
  <div class="abs brand">VORNAK</div>
  <div class="abs top-contact" style="left:770px"><i></i>+27(0)110004821</div>
  <div class="abs top-contact" style="left:955px"><i></i>info@vornak.example</div>
  <nav>
    <span class="abs main-nav" style="left:663px">Home</span>
    <span class="abs main-nav" style="left:780px">About</span>
    <span class="abs main-nav" style="left:895px">Projects</span>
    <span class="abs main-nav" style="left:1025px">Contacts</span>
  </nav>
</header>

<!-- Hero -->
<section class="abs hero" role="img" aria-label="Photo of a small wooden house model resting on a laptop keyboard beside a potted plant"></section>
<svg class="abs" style="left:0;top:680px" width="1200" height="110" viewBox="0 0 1200 110"><polygon points="0,10 600,102 1200,10 1200,110 0,110" fill="#ffffff"/></svg>
<div class="abs slide-arrow" style="left:0"><svg width="36" height="38"><polyline points="22,12 14,19 22,26" fill="none" stroke="#fff" stroke-width="2"/></svg></div>
<div class="abs slide-arrow" style="left:1164px"><svg width="36" height="38"><polyline points="22,12 14,19 22,26" fill="none" stroke="#fff" stroke-width="2"/></svg></div>
<h1 class="abs hero-title">PROPERTY<br>DEVELOPMENT</h1>
<div class="abs btn hero-btn">CALL US TODAY</div>

<!-- Welcome -->
<h2 class="abs section-title" style="top:852px"><span class="soft">WELCOME TO</span> <span style="color:var(--blue);font-weight:700">VORNAK</span></h2>
<div class="abs rule" style="top:940px"></div>
<div class="abs rule-dot" style="top:935px"></div>
<p class="abs lead" style="top:968px">Lorem Ipsum is simply dummy text of the printing and typesetting industry. Lorem Ipsum has been the industry's standard dummy text ever since the 1500s, when an unknown printer took a galley of type and scrambled it to make a type specimen book. It has survived not only five cent electronic typesetting, remaining essentially unchanged.. as survived not only five centuries, but also the leap in as survived not only five cen.</p>

<svg class="abs" style="left:148px;top:1085px" width="75" height="90" viewBox="0 0 75 90">
  <rect x="8" y="10" width="52" height="20" rx="6" transform="rotate(-25 34 20)" fill="#1c9ad6"/>
  <line x1="36" y1="34" x2="22" y2="86" stroke="#111" stroke-width="4"/>
  <line x1="36" y1="34" x2="50" y2="86" stroke="#111" stroke-width="4"/>
  <line x1="36" y1="34" x2="36" y2="86" stroke="#111" stroke-width="4"/>
</svg>
<div class="abs pillar-title" style="left:235px;top:1085px"><span class="soft">OUR</span> VISION</div>
<div class="abs rule" style="left:235px;top:1115px;width:345px"></div>
<p class="abs pillar-text" style="left:235px;top:1134px">Lorem Ipsum is simply dummy text of the ng and typesetting industry. Lorem Ipsum has be the industry's standard dummy text ever since the 1500s, when.</p>

<svg class="abs" style="left:608px;top:1100px" width="76" height="70" viewBox="0 0 76 70">
  <circle cx="34" cy="36" r="30" fill="none" stroke="#1c9ad6" stroke-width="6"/>
  <circle cx="34" cy="36" r="19" fill="none" stroke="#111" stroke-width="5"/>
  <circle cx="34" cy="36" r="8" fill="#1c9ad6"/>
  <line x1="34" y1="36" x2="68" y2="6" stroke="#111" stroke-width="4"/>
</svg>
<div class="abs pillar-title" style="left:697px;top:1085px"><span class="soft">OUR</span> MISSION</div>
<div class="abs rule" style="left:697px;top:1115px;width:345px"></div>
<p class="abs pillar-text" style="left:697px;top:1134px">Lorem Ipsum is simply dummy text of the ng and typesetting industry. Lorem Ipsum has be the industry's standard dummy text ever since the 1500s, when.</p>

<div class="abs btn read-btn">READ MORE</div>

<!-- Services -->
<section class="abs services"></section>
<svg class="abs" style="left:0;top:2045px" width="1200" height="106" viewBox="0 0 1200 106"><polygon points="0,0 1200,0 600,105" fill="#222222"/></svg>
<h2 class="abs section-title services-title"><span class="soft">OUR</span> SERVICES</h2>
<div class="abs rule" style="top:1500px;background:#444"></div>
<div class="abs rule-dot" style="top:1495px"></div>

<svg class="abs" style="left:0;top:1540px" width="1200" height="500" viewBox="0 0 1200 500">
  <defs>
    <linearGradient id="gProp" x1="0" y1="0" x2="1" y2="1"><stop offset="0" stop-color="#8b6a5a"/><stop offset="1" stop-color="#e9e7e4"/></linearGradient>
    <linearGradient id="gHouse" x1="0" y1="0" x2="0" y2="1"><stop offset="0" stop-color="#c9d4de"/><stop offset="1" stop-color="#c48a52"/></linearGradient>
    <linearGradient id="gDemo" x1="0" y1="0" x2="1" y2="1"><stop offset="0" stop-color="#c69a3a"/><stop offset="1" stop-color="#7a5a44"/></linearGradient>
    <linearGradient id="gMine" x1="0" y1="0" x2="0" y2="1"><stop offset="0" stop-color="#e3c9b0"/><stop offset="1" stop-color="#8d5a3c"/></linearGradient>
    <linearGradient id="gShip" x1="0" y1="0" x2="0" y2="1"><stop offset="0" stop-color="#dfe3e6"/><stop offset="1" stop-color="#7a3a30"/></linearGradient>
    <linearGradient id="gBrick" x1="0" y1="0" x2="1" y2="1"><stop offset="0" stop-color="#8f8f8f"/><stop offset="1" stop-color="#c7c3bd"/></linearGradient>
    <linearGradient id="gMix" x1="0" y1="0" x2="1" y2="1"><stop offset="0" stop-color="#b8a48c"/><stop offset="1" stop-color="#6f5d4a"/></linearGradient>
  </defs>
  <g role="img" aria-label="Property development service photo">
    <polygon points="230,7 349,75 349,212 230,280 111,212 111,75" fill="url(#gProp)"/>
    <polygon points="230,7 349,75 349,212 230,280 111,212 111,75" fill="#ffffff" fill-opacity=".25"/>
  </g>
  <polygon role="img" aria-label="Photo of a finished residential house" points="472,7 591,75 591,212 472,280 353,212 353,75" fill="url(#gHouse)"/>
  <polygon role="img" aria-label="Photo of an excavator during demolition" points="714,7 833,75 833,212 714,280 595,212 595,75" fill="url(#gDemo)"/>
  <polygon role="img" aria-label="Photo of a mining haul truck" points="956,7 1075,75 1075,212 956,280 837,212 837,75" fill="url(#gMine)"/>
  <polygon role="img" aria-label="Photo of transport by ship and plane" points="351,213 470,281 470,418 351,486 232,418 232,281" fill="url(#gShip)"/>
  <polygon role="img" aria-label="Photo of concrete paving bricks being laid" points="593,213 712,281 712,418 593,486 474,418 474,281" fill="url(#gBrick)"/>
  <polygon role="img" aria-label="Photo of ready-mix concrete being poured" points="835,213 954,281 954,418 835,486 716,418 716,281" fill="url(#gMix)"/>
</svg>
<div class="abs hex-label">
  <h3>PROPERTY<br>DEVELOPMENT</h3>
  <p>Lorem Ipsum is simply dummy text of<br>the ng and typesetting.</p>
</div>

<!-- Testimonials -->
<h2 class="abs section-title testi-title"><span class="soft">CLIENT</span> TESTIMONIALS</h2>
<div class="abs rule" style="top:2292px"></div>
<div class="abs rule-dot" style="top:2283px"></div>
<svg class="abs" style="left:545px;top:2347px" width="112" height="126" viewBox="0 0 112 126" role="img" aria-label="Portrait of the client">
  <defs><linearGradient id="gAvatar" x1="0" y1="0" x2="0" y2="1"><stop offset="0" stop-color="#d9d9d9"/><stop offset="1" stop-color="#7c7c7c"/></linearGradient></defs>
  <polygon points="56,1 111,32 111,94 56,125 1,94 1,32" fill="url(#gAvatar)"/>
</svg>
<div class="abs quote-mark" style="left:126px;top:2480px">“</div>
<p class="abs quote">Lorem Ipsum is simply dummy text of the printing and typesetting industry. Lorem Ipsum has been the industry's standard dummy text ever since the 1500s, when an unknown printer took a galley of type and scrambled it to make a type specimen book. It has survived not only five cent electronic typesetting, remaining essentially unchanged.. as survived not only five centuries, but also the leap in as survived not only five cen.</p>
<div class="abs quote-mark" style="left:1008px;top:2550px">”</div>
<div class="abs client-name">Typesetting Galley</div>
<div class="abs client-role">Lorem Ipsum is simply dummy</div>

<!-- Footer -->
<footer class="footer">
  <svg class="abs" style="left:0;top:2742px" width="1200" height="100" viewBox="0 0 1200 100"><polygon points="600,0 1200,99 0,99" fill="#0c0c0c"/></svg>
  <div class="abs footer-bg"></div>
  <div class="abs brand">VORNAK</div>

  <h4 class="abs foot-h" style="left:113px;top:2985px">ADDRESS</h4>
  <div class="abs addr-row" style="top:3025px">
    <svg width="16" height="22" viewBox="0 0 16 22"><path d="M8 0a8 8 0 0 0-8 8c0 6 8 14 8 14s8-8 8-14a8 8 0 0 0-8-8z" fill="#1c9ad6"/><circle cx="8" cy="8" r="3" fill="#0c0c0c"/></svg>
    <p class="foot-text" style="width:215px">Lorem Ipsum is simply dummy text the printing and typesetting industry. Lorem Ipsum has been.</p>
  </div>
  <div class="abs addr-row" style="top:3098px">
    <svg width="16" height="16" viewBox="0 0 16 16"><path d="M3 1l3 0 1 4-2 1.5a9 9 0 0 0 4.5 4.5L11 9l4 1v3a2 2 0 0 1-2 2C6 15 1 10 1 3a2 2 0 0 1 2-2z" fill="#1c9ad6"/></svg>
    <p class="foot-text">+27(0)110004821</p>
  </div>
  <div class="abs addr-row" style="top:3124px">
    <svg width="16" height="16" viewBox="0 0 16 16"><rect x="3" y="0" width="10" height="5" fill="#1c9ad6"/><rect x="0" y="5" width="16" height="7" rx="1" fill="#1c9ad6"/><rect x="3" y="10" width="10" height="6" fill="#fff"/></svg>
    <p class="foot-text">+27(0)110004822</p>
  </div>
  <div class="abs addr-row" style="top:3150px">
    <svg width="16" height="12" viewBox="0 0 16 12"><rect width="16" height="12" fill="#1c9ad6"/><polyline points="0,0 8,7 16,0" fill="none" stroke="#0c0c0c" stroke-width="1.5"/></svg>
    <p class="foot-text">info@vornak.example</p>
  </div>

  <p class="abs foot-text" style="left:430px;top:3016px;width:230px">Ipsum is simply dummy text thprinting and typesetting industry.</p>
  <div class="abs sub-input"></div>
  <div class="abs btn" style="left:430px;top:3118px;width:105px;height:32px">SIGN UP</div>

  <div class="abs rule" style="left:113px;top:3202px;width:542px;background:#444"></div>
  <p class="abs foot-text" style="left:113px;top:3242px">Follow Us On:</p>
  <div class="abs social">
    <i style="width:32px;height:32px;background:#ffffff"></i>
    <i style="width:12px;height:12px;background:#777"></i>
    <i style="width:12px;height:12px;background:#777"></i>
    <i style="width:12px;height:12px;background:#777"></i>
    <i style="width:12px;height:12px;background:#777"></i>
  </div>

  <h4 class="abs foot-h" style="left:703px;top:2985px">CONTACT US</h4>
  <div class="abs field" style="top:3023px">Name</div>
  <div class="abs field" style="top:3067px">Email</div>
  <div class="abs field" style="top:3111px">Phone</div>
  <div class="abs field" style="top:3155px;height:104px">Message</div>
  <div class="abs btn" style="left:703px;top:3283px;width:84px;height:34px">SUBMIT</div>
</footer>

<nav class="abs bottom-nav">
  <span style="left:387px">Home</span>
  <span style="left:502px">About</span>
  <span style="left:618px">Projects</span>
  <span style="left:748px">Contacts</span>
</nav>

</body>
</html>
```